Oil and Gas Company: Letterhead Design

In short we need a professional company letterhead designed for our Oil and Gas company.

We would like to keep the design simple and professional. Letterhead to include the company logo and color scheme, front page and continuation pages.

For reference, see attached logo below with our company logo and color scheme.

Target Market(s)

Oil & Gas Market

Industry/Entity Type

Oil And Gas

Font styles to use
Sans Serif

Requirements
Must have
• Letterhead must contain a front page & continuation page.
• Must be simple and professional in design.
• Follow our logo and color scheme.
Nice to have
• I would like to have the logo embedded in the bottom right hand portion of the page to provide some depth into the letterhead.

```html
<!DOCTYPE html>
<html lang="en">
<head>
<meta charset="utf-8">
<title>Meridian Wellfield Services – Letterhead</title>
<link href="https://fonts.googleapis.com/css2?family=Roboto:wght@400;500&family=Mulish:wght@500&display=swap" rel="stylesheet">
<style>
:root{
  --brand-blue:#1553a6;
  --brand-red:#e4242b;
  --paper:#f3f3f3;
  --ink:#1b1b1b;
  --muted:#555a60;
  --backdrop:#e6e8ec;
}
*{box-sizing:border-box;margin:0;padding:0}
html,body{width:1200px;height:1000px;overflow:hidden}
body{background:var(--backdrop);position:relative;font-family:"Mulish",sans-serif}
.sheet{position:absolute;top:126px;width:528px;height:746px;background:var(--paper);overflow:hidden}
.sheet--front{left:65px}
.sheet--continuation{left:632px}
.header-accent{position:absolute;left:45px;top:34px;width:7px;height:108px;border-radius:4px;background:var(--brand-red)}
.company-name{position:absolute;left:67px;top:51px;font-family:"Roboto",sans-serif;font-weight:500;font-size:11.5px;line-height:12.5px;color:var(--brand-blue);text-transform:uppercase}
.contact{position:absolute;left:67px;top:91px;font-family:"Roboto",sans-serif;font-size:10.5px;line-height:12px;color:var(--muted);list-style:none}
.letter-body{position:absolute;font-size:8.45px;line-height:9.65px;color:var(--ink);text-align:justify;hyphens:auto}
.letter-body p+p{margin-top:9.6px}
.sheet--front .letter-body{left:48px;top:226px;width:437px}
.sheet--continuation .letter-body{left:45px;top:42px;width:440px}
.footer-band{position:absolute;left:0;height:33px;background:var(--brand-blue)}
.sheet--front .footer-band{top:694px;width:351px}
.sheet--continuation .footer-band{top:696px;width:353px}
.footer-block{position:absolute;right:0;width:43px;height:33px;background:var(--brand-red)}
.sheet--front .footer-block{top:694px}
.sheet--continuation .footer-block{top:696px;right:0;width:41px}
.footer-name{position:absolute;font-family:"Roboto",sans-serif;font-weight:500;font-size:11px;line-height:12.5px;color:#23272e;text-align:center;text-transform:uppercase;width:134px}
.sheet--front .footer-name{left:350px;top:697px}
.sheet--continuation .footer-name{left:353px;top:699px}
</style>
</head>
<body>

<section class="sheet sheet--front" aria-label="Letterhead front page">
  <div class="header-accent"></div>
  <h1 class="company-name">Meridian<br>Wellfield Services</h1>
  <ul class="contact">
    <li>(01) 555 014 270</li>
    <li>office@meridianwell.com</li>
    <li>www.meridianwell.com</li>
  </ul>
  <div class="letter-body">
    <p>Lorem ipsum dolor sit amet, consectetur adipiscing elit. Integer a felis sapien. Fusce massa velit, sollicitudin eget vestibulum sit amet, dictum eu est. Proin et laoreet erat. Praesent at ex velit. Proin sit amet ex ac felis condimentum tincidunt at et justo. Cras et nulla mauris. Lorem ipsum dolor sit amet, consectetur adipiscing elit. Integer consequat lectus elit, condimentum faucibus augue eleifend convallis. Nullam interdum ante vel orci ultrices, in commodo nunc sollicitudin. Vestibulum nisi ante, hendrerit feugiat sem id, congue dictum diam. Mauris dapibus euismod lectus, sit amet laoreet diam feugiat eget. Etiam quis consectetur neque. Etiam posuere magna ut nisl sodales, eu luctus metus mollis.</p>
    <p>Proin facilisis sit amet enim ut gravida. Donec id imperdiet ligula. Vivamus est augue, pretium id velit vehicula, ullamcorper mollis tortor. Integer ligula metus, blandit porta varius ac, hendrerit eget nulla. Morbi et dictum est. Curabitur nulla elit, pulvinar ac finibus non, varius a odio. Vestibulum ante ipsum primis in faucibus orci luctus et ultrices posuere cubilia Curae; Aenean pulvinar sapien et nulla congue, vitae eleifend metus vestibulum. Suspendisse elementum feugiat sagittis. Fusce ornare urna rutrum, congue sem et, vulputate enim. Aliquam erat volutpat. Etiam at pellentesque neque, at pulvinar orci.</p>
    <p>Phasellus eleifend arcu ac tellus imperdiet, et convallis lacus lobortis. Ut quis dolor in odio porta ullamcorper. Mauris id porta ex, sed euismod sapien. Fusce non luctus mi, quis auctor orci. Orci varius natoque penatibus et magnis dis parturient montes, nascetur ridiculus mus. Duis vel diam augue. Curabitur dignissim lorem eu nisl malesuada, quis commodo elit convallis. Vestibulum consequat blandit vulputate. Integer vel hendrerit purus. Mauris interdum eu lacus ut efficitur. Maecenas nunc lacus, laoreet et quam vitae, sollicitudin malesuada urna. Sed dapibus ante non libero cursus ultricies. Suspendisse quis viverra nisi. Suspendisse dapibus aliquam est mattis blandit.</p>
    <p>Maecenas euismod quam magna, quis pretium justo lobortis quis. Integer convallis dignissim sapien, et vestibulum risus accumsan a. Ut mi sem, ullamcorper at metus at, efficitur bibendum libero. Fusce imperdiet a dolor suscipit efficitur. Praesent venenatis ex et felis maximus, in pretium libero volutpat. Nullam iaculis ut ex sed bibendum. Aenean eget condimentum lectus. Integer mauris erat, volutpat eu dui vitae, egestas finibus justo. Nam vel auctor augue.</p>
  </div>
  <div class="footer-band"></div>
  <div class="footer-name">Meridian<br>Wellfield Services</div>
  <div class="footer-block"></div>
</section>

<section class="sheet sheet--continuation" aria-label="Letterhead continuation page">
  <div class="letter-body">
    <p>Lorem ipsum dolor sit amet, consectetur adipiscing elit. Integer a felis sapien. Fusce massa velit, sollicitudin eget vestibulum sit amet, dictum eu est. Proin et laoreet erat. Praesent at ex velit. Proin sit amet ex ac felis condimentum tincidunt at et justo. Cras et nulla mauris. Lorem ipsum dolor sit amet, consectetur adipiscing elit. Integer consequat lectus elit, condimentum faucibus augue eleifend convallis. Nullam interdum ante vel orci ultrices, in commodo nunc sollicitudin. Vestibulum nisi ante, hendrerit feugiat sem id, congue dictum diam. Mauris dapibus euismod lectus, sit amet laoreet diam feugiat eget. Etiam quis consectetur neque. Etiam posuere magna ut nisl sodales, eu luctus metus mollis.</p>
    <p>Proin facilisis sit amet enim ut gravida. Donec id imperdiet ligula. Vivamus est augue, pretium id velit vehicula, ullamcorper mollis tortor. Integer ligula metus, blandit porta varius ac, hendrerit eget nulla. Morbi et dictum est. Curabitur nulla elit, pulvinar ac finibus non, varius a odio. Vestibulum ante ipsum primis in faucibus orci luctus et ultrices posuere cubilia Curae; Aenean pulvinar sapien et nulla congue, vitae eleifend metus vestibulum. Suspendisse elementum feugiat sagittis. Fusce ornare urna rutrum, congue sem et, vulputate enim. Aliquam erat volutpat. Etiam at pellentesque neque, at pulvinar orci.</p>
    <p>Phasellus eleifend arcu ac tellus imperdiet, et convallis lacus lobortis. Ut quis dolor in odio porta ullamcorper. Mauris id porta ex, sed euismod sapien. Fusce non luctus mi, quis auctor orci. Orci varius natoque penatibus et magnis dis parturient montes, nascetur ridiculus mus. Duis vel diam augue. Curabitur dignissim lorem eu nisl malesuada, quis commodo elit convallis. Vestibulum consequat blandit vulputate. Integer vel hendrerit purus. Mauris interdum eu lacus ut efficitur. Maecenas nunc lacus, laoreet et quam vitae, sollicitudin malesuada urna. Sed dapibus ante non libero cursus ultricies. Suspendisse quis viverra nisi. Suspendisse dapibus aliquam est mattis blandit.</p>
    <p>Maecenas euismod quam magna, quis pretium justo lobortis quis. Integer convallis dignissim sapien, et vestibulum risus accumsan a. Ut mi sem, ullamcorper at metus at, efficitur bibendum libero. Fusce imperdiet a dolor suscipit efficitur. Praesent venenatis ex et felis maximus, in pretium libero volutpat. Nullam iaculis ut ex sed bibendum. Aenean eget condimentum lectus. Integer mauris erat, volutpat eu dui vitae, egestas finibus justo. Nam vel auctor augue.</p>
    <p>ullamcorper mollis tortor. Integer ligula metus, blandit porta varius ac, hendrerit eget nulla. Morbi et dictum est. Curabitur nulla elit, pulvinar ac finibus non, varius a odio. Vestibulum ante ipsum primis in faucibus orci luctus et ultrices posuere cubilia Curae; Aenean pulvinar sapien et nulla congue, vitae eleifend metus vestibulum. Suspendisse elementum feugiat sagittis. Fusce ornare urna rutrum, congue sem et, vulputate enim. Aliquam erat volutpat. Etiam at pellentesque neque, at pulvinar orci.</p>
    <p>Phasellus eleifend arcu ac tellus imperdiet, et convallis lacus lobortis. Ut quis dolor in odio porta ullamcorper. Mauris id porta ex, sed euismod sapien. Fusce non luctus mi, quis auctor orci. Orci varius natoque penatibus et magnis dis parturient montes, nascetur ridiculus mus. Duis vel diam augue. Curabitur dignissim lorem eu nisl malesuada, quis commodo elit convallis. Vestibulum consequat blandit vulputate. Integer vel hendrerit purus. Mauris interdum eu lacus ut efficitur. Maecenas nunc lacus, laoreet et quam vitae, sollicitudin malesuada urna. Sed dapibus ante non libero cursus ultricies. Suspendisse quis viverra nisi. Suspendisse dapibus aliquam est mattis blandit.</p>
    <p>Maecenas euismod quam magna, quis pretium justo lobortis quis. Integer convallis dignissim sapien, et vestibulum risus accumsan a. Ut mi sem, ullamcorper at metus at, efficitur bibendum libero. Fusce imperdiet a dolor suscipit efficitur. Praesent venenatis ex et felis maximus, in pretium libero volutpat. Nullam iaculis ut ex sed bibendum. Aenean eget condimentum lectus. Integer mauris erat, volutpat eu dui vitae, egestas finibus justo. Nam vel auctor augue.</p>
  </div>
  <div class="footer-band"></div>
  <div class="footer-name">Meridian<br>Wellfield Services</div>
  <div class="footer-block"></div>
</section>

</body>
</html>
```